Business Card Design Project

We are not a new company, but renamed to "Norvane Kitchens" last year. We specialize in modern high-end cabinetry imports. We would like to communicate a sense of quality and cutting edge technology. Ideally the design would incorporate our logo colors, silver, red and preferably a black, matte background. Though we are open to suggestions.
Logo is attached.
Edit: I have attached rough drafts of the previous cards, this way you will have all necessary content that needs to go on the cards.
Updates
Project Deadline Extended
Reason: We have received a lot of great designs, but due to the sheer number we couldn't respond to all. We will extend the deadline for another 7 days to finalize and provide feedback to designers.
Thank you for your hard work!
Industry/Entity Type
Business
Look and feel
Each slider illustrates characteristics of the customer's brand and the style your logo design should communicate.

```html
<!DOCTYPE html>
<html lang="en">
<head>
<meta charset="utf-8">
<title>Norvane Kitchens — Business Card</title>
<link rel="stylesheet" href="https://fonts.googleapis.com/css2?family=Open+Sans:wght@400;600;700&display=swap">
<style>
  :root {
    --stage: #1c1c1c;
    --card-top: #222224;
    --card-bottom: #0b0b0c;
    --silver: #c9cbcd;
    --silver-dim: #8d9093;
    --red: #d0141c;
    --white: #f2f2f2;
  }
  * { box-sizing: border-box; margin: 0; padding: 0; }
  html, body {
    width: 1200px; height: 900px; overflow: hidden;
    background: var(--stage);
    font-family: "Open Sans", Arial, sans-serif;
  }
  .stage {
    width: 1200px; height: 900px;
    display: flex; flex-direction: column; align-items: center; justify-content: center;
    gap: 48px;
  }
  .card {
    position: relative;
    width: 660px; height: 378px;
    border-radius: 16px;
    background: linear-gradient(160deg, var(--card-top) 0%, var(--card-bottom) 100%);
    box-shadow: 0 12px 30px rgba(0,0,0,.55);
    overflow: hidden;
  }
  .wordmark {
    display: flex; align-items: center; gap: 10px;
    color: var(--silver);
    font-weight: 600;
    text-transform: uppercase;
    letter-spacing: .12em;
    white-space: nowrap;
  }
  .wordmark__square {
    width: 14px; height: 14px; background: var(--silver); flex: none;
  }

  /* contact side */
  .brand-panel {
    position: absolute; left: 0; top: 0;
    width: 340px; height: 100%;
    display: flex; align-items: center; justify-content: center;
    padding-top: 90px;
  }
  .card--contact .wordmark { font-size: 17px; }
  .card--contact .divider {
    position: absolute; left: 340px; top: 36px;
    width: 1px; height: 306px;
    background: linear-gradient(to bottom, var(--red) 0%, var(--red) 45%, rgba(208,20,28,.15) 100%);
  }
  .person { position: absolute; left: 370px; top: 46px; }
  .person__name { color: var(--red); font-weight: 700; font-size: 28px; line-height: 1.1; }
  .person__role { color: var(--white); font-size: 13px; margin-top: 6px; }
  .contact-list { list-style: none; margin-top: 24px; }
  .contact-list li {
    display: flex; gap: 20px;
    color: var(--white); font-size: 14px; line-height: 1.45;
  }
  .contact-list .label { width: 12px; font-weight: 600; color: var(--silver-dim); }
  .contact-list .indent { padding-left: 32px; }

  /* logo side */
  .card--logo .wordmark {
    position: absolute; left: 0; right: 0; top: 136px;
    justify-content: center; font-size: 40px; gap: 18px;
  }
  .card--logo .wordmark__square { width: 28px; height: 28px; }
  .card--logo .rule {
    position: absolute; left: 70px; right: 50px; top: 250px; height: 1px;
    background: linear-gradient(to right, var(--red) 0%, var(--red) 35%, var(--silver-dim) 100%);
  }
</style>
</head>
<body>
<main class="stage">
  <section class="card card--contact" aria-label="Business card, contact side">
    <div class="brand-panel">
      <div class="wordmark"><span class="wordmark__square"></span>Norvane Kitchens</div>
    </div>
    <div class="divider"></div>
    <div class="person">
      <p class="person__name">Marek Dovan</p>
      <p class="person__role">President</p>
      <ul class="contact-list">
        <li><span class="label">P</span><span>555.210.0148</span></li>
        <li><span class="label">F</span><span>555.210.0172</span></li>
        <li><span class="label">C</span><span>555.386.2047</span></li>
        <li><span class="label">E</span><span>marek@norvanekitchens.ca</span></li>
        <li><span class="label">A</span><span>2150 - 87 St.</span></li>
        <li><span class="indent">Westmere, AB T4K 2M9</span></li>
      </ul>
    </div>
  </section>

  <section class="card card--logo" aria-label="Business card, logo side">
    <div class="wordmark"><span class="wordmark__square"></span>Norvane Kitchens</div>
    <div class="rule"></div>
  </section>
</main>
</body>
</html>
```